Creative Brief
tarnell financial llc .com
tarnellfinancial.example
I need double sided standard sized Business Card [3.5" x 2"]
just keep logo in mind
Professional
Dale Tarnell
President
4178 E. K Ave.
Greeley, CO 80219
dale@tarnellfinancial.example
I was in a logo contest, please utilize that design
as you see fit

```html
<!DOCTYPE html>
<html lang="en">
<head>
<meta charset="utf-8">
<title>Tarnell Financial — Business Card</title>
<link rel="stylesheet" href="https://fonts.googleapis.com/css2?family=Arimo:wght@400;700&display=swap">
<style>
  :root {
    --backdrop: #e9e6e1;
    --card: #ffffff;
    --brand-blue: #1c6aa8;
    --brand-green: #2f9a3e;
    --ink: #3a3a3a;
    --icon: #4a4a4a;
    --rule: #c9c9c9;
  }
  * { margin: 0; padding: 0; box-sizing: border-box; }
  html, body {
    width: 1200px;
    height: 778px;
    overflow: hidden;
    background: var(--backdrop);
    font-family: "Arimo", Arial, sans-serif;
  }
  .card {
    position: absolute;
    left: 110px;
    top: 108px;
    width: 980px;
    height: 562px;
    background: var(--card);
    box-shadow: 0 2px 10px rgba(0,0,0,0.12);
  }
  .brand {
    position: absolute;
    left: 0;
    right: 0;
    top: 62px;
    display: flex;
    flex-direction: column;
    align-items: center;
    gap: 22px;
  }
  .brand-mark {
    width: 112px;
    height: 112px;
    background: var(--brand-blue);
  }
  .brand-name {
    font-size: 34px;
    font-weight: 700;
    letter-spacing: 0.5px;
    color: var(--brand-blue);
  }
  .holder {
    position: absolute;
    right: 535px;
    top: 374px;
    text-align: right;
  }
  .holder-name {
    font-size: 30px;
    font-weight: 700;
    color: var(--brand-blue);
  }
  .holder-title {
    margin-top: 8px;
    font-size: 23px;
    font-weight: 700;
    color: var(--brand-green);
  }
  .divider {
    position: absolute;
    left: 490px;
    top: 318px;
    width: 1px;
    height: 192px;
    background: var(--rule);
  }
  .address {
    position: absolute;
    left: 539px;
    top: 324px;
    font-size: 23px;
    line-height: 40px;
    color: var(--ink);
  }
  .contacts {
    position: absolute;
    left: 539px;
    top: 408px;
    list-style: none;
    font-size: 23px;
    line-height: 35px;
    color: var(--ink);
  }
  .contacts li {
    display: flex;
    align-items: center;
    gap: 12px;
  }
  .contacts svg {
    width: 18px;
    height: 18px;
    fill: var(--icon);
    flex: none;
  }
</style>
</head>
<body>
  <div class="card">
    <div class="brand">
      <div class="brand-mark"></div>
      <div class="brand-name">TARNELL FINANCIAL LLC .COM</div>
    </div>

    <div class="holder">
      <div class="holder-name">Dale Tarnell</div>
      <div class="holder-title">President</div>
    </div>

    <div class="divider"></div>

    <div class="address">
      <div>4178 E. K Ave.</div>
      <div>Greeley, CO 80219</div>
    </div>

    <ul class="contacts">
      <li>
        <svg viewBox="0 0 24 24" aria-hidden="true"><path d="M6.6 10.8c1.4 2.8 3.8 5.1 6.6 6.6l2.2-2.2c.3-.3.7-.4 1-.2 1.1.4 2.3.6 3.6.6.6 0 1 .4 1 1V20c0 .6-.4 1-1 1C10.6 21 3 13.4 3 4c0-.6.4-1 1-1h3.5c.6 0 1 .4 1 1 0 1.3.2 2.5.6 3.6.1.3 0 .7-.2 1L6.6 10.8z"/></svg>
        <span>970-555-0142</span>
      </li>
      <li>
        <svg viewBox="0 0 24 24" aria-hidden="true"><path d="M2 5h20v14H2V5zm2 2v.5l8 5 8-5V7H4zm0 2.8V17h16V9.8l-8 5-8-5z"/></svg>
        <span>dale@tarnellfinancial.example</span>
      </li>
      <li>
        <svg viewBox="0 0 24 24" aria-hidden="true"><circle cx="12" cy="12" r="10"/><path d="M12 2c-3 3-3 17 0 20M12 2c3 3 3 17 0 20M2 12h20M4 7h16M4 17h16" stroke="#fff" stroke-width="1.3" fill="none"/></svg>
        <span>www.tarnellfinancial.example</span>
      </li>
    </ul>
  </div>
</body>
</html>
```